Creative UI design for web application

I need a new UI design for my web application. It will be used by small and micro business owners to plan & implement growth tactics.

I've attached the current design (which I'm open to be changed) - but in particular I need to design the centre of the screen, where the work actually happens.

There needs to be place for a title (YOUR BUSINESS) and description (say 1-2 paragraphs of text) - and am happy to include icons or imagery where makes sense. It may make sense for the user to be able to upload their business logo and name, for example.

This screen will be used by the business owner to understand the real value they offer potential customers and their point of difference - why they exist and why potential customers should care.

They'll use the information they put into this screen to plan things like their messaging.

Following that, there needs to be 2 sections in the dashboard.

The first section is titled "WHO YOU ARE"

The first section will include a number of boxes that the user can input information into, as follows:

- Logo
- Business name
- Business tag line
- Business vision
- Business bio
- Brand colours (these should end up as swatches based on the colour code they enter) - the colour code for each colour swatch should also be visible.
- Key competitors
- SWOT analysis (boxes to enter their strengths, weaknesses, opportunities and threats).

The second section is titled "WHY YOU EXIST"

The second section will include a number of boxes that the user can input information (text) into, as follows:

- Who are your ideal customers?
- What problem are you trying to solve for them?
- What pain points will this remove for them?
- How do you solve it?
- How else could this problem be solved?
- Who offers these other solutions?
- Why is your solution better?
- How much does your solution cost?
- What value are you providing to justify this cost?
- How will this make their life/job easier/better?

They should be able to write a decent amount of information in the boxes.

There should ideally be a place for a description for each of these text fields (for both section 1 & 2) as well so I can give them a little bit more direction around what to put in the box. Alternatively there could be a little icon (say a question mark or "i") that they could click on to view instructions. The instructions will be around 2-4 sentences long for each text field.

You have 2 options:

a) This all needs to appear on the one screen, and the navigation needs to be visible (as per the example attached but feel free to recreate this navigation)

Note: the page can scroll below the fold - but please provide the design for the full length of the page.

b) Potentially the 2 sections could actually be in 2 different items in the menu - YOUR BUSINESS and YOUR VALUE (which would sit next to YOUR BUSINESS and before YOUR CUSTOMER in the screenshot provided). feel free to design them as 2 separate screens if you prefer.

I have attached a screenshot of the app as it stands today (screen shot 2017) which would still exist in the new design but under a different section (the learn section from the plan2 mockup attached)

I have mocked up how this new screen could look if broken into 2 and that's also attached. If you can make this come to life - and look more engaging that would be helpful! :)

Target Market(s)

Small and micro business owners

Industry/Entity Type

Marketing

Number of Pages Required

1 page

Font styles to use
Sans Serif
Other font styles liked:
• Montserrat

Colors
87cfc6
d2a4cc
ffffff
85cae6
e8e8e8
5c5c5c

Requirements
Must have
• Use of my brand colours: #cc8eb2, #76d6c8, #68c7ff as well as white and #595959. Must be visually pleasing / engaging, designed for desktop (as it's a desktop application), really easy to use / navigate.
• Use font Montserrat light & Montserrat Regular or Bold. Mostly should be Montserrat light.
Nice to have
• Would be nice to see how this would look on mobile (as the application is responsive) but this is not mandatory.
Should not have
• Should not look too corporate or dry.

```html
<!DOCTYPE html>
<html lang="en">
<head>
<meta charset="utf-8">
<title>Bloomwise – Who You Are</title>
<link href="https://fonts.googleapis.com/css2?family=Montserrat:wght@300;400;600;700&display=swap" rel="stylesheet">
<style>
:root{
  --dark:#3f3f3f;--side:#595959;--light:#e8e8e8;--white:#fff;--page:#fff;
  --pink:#cc8eb2;--pink-deep:#b9518a;--teal:#76d6c8;--teal-deep:#3eab99;
  --blue:#68c7ff;--blue-deep:#3a9cc9;--grey-btn:#555;--ink:#595959;
}
*{box-sizing:border-box;margin:0;padding:0}
html,body{width:1200px;height:712px;overflow:hidden}
body{font-family:'Montserrat',sans-serif;font-weight:300;color:var(--ink);background:var(--page);position:relative}
.abs{position:absolute}
.topbar{left:0;top:0;width:1200px;height:43px;background:var(--dark);color:#fff}
.brand{left:0;top:0;width:188px;height:43px;display:flex;align-items:center;justify-content:center;font-size:15px;font-weight:400;letter-spacing:.5px;border-bottom:1px solid #777}
.tab{top:0;height:43px;display:flex;align-items:center;justify-content:center;font-size:12px;font-weight:400}
.tab.active{background:var(--pink);left:188px;width:93px}
.account{right:24px;top:0;height:43px;display:flex;align-items:center;gap:10px;font-size:12px;font-weight:400}
.sidebar{left:0;top:43px;width:188px;height:669px;background:var(--side);color:#fff;font-size:9.5px;font-weight:400}
.nav-item{height:30px;display:flex;align-items:center;padding-left:22px;gap:10px}
.nav-item.light{background:var(--light);color:var(--ink)}
.nav-sub{height:22px;display:flex;align-items:center;padding-left:38px;gap:8px;background:#f4f4f4;color:var(--ink);font-size:8.5px}
.nav-sub.alt{background:var(--light)}
.ico{width:9px;height:9px;border-radius:50%;border:1.5px solid currentColor;flex:none}
.copyright{left:0;bottom:28px;width:188px;text-align:center;font-size:7.5px;line-height:10px}
.card{position:absolute;overflow:hidden}
.card-head{height:37px;display:flex;align-items:center;justify-content:center;color:#fff;font-size:11px;font-weight:600;letter-spacing:1px}
.hint{color:#fff;font-size:8.5px;line-height:10px;padding:8px 7px 0}
.field{background:#fff;position:absolute}
.profile{left:198px;top:54px;width:187px;height:363px;background:var(--blue)}
.logo-ring{left:33px;top:19px;width:120px;height:120px;border-radius:50%;background:#fff;border:2px solid #2f84b4;display:flex;align-items:center;justify-content:center;font-size:15px;font-weight:400;color:#333}
.profile-name{top:155px;width:187px;text-align:center;color:#fff;font-size:18px;font-weight:600;letter-spacing:1px}
.contact{left:0;width:187px;height:34px;background:#eee;display:flex;align-items:center;font-size:9px;font-weight:400;letter-spacing:.3px}
.contact .badge{width:38px;height:34px;display:flex;align-items:center;justify-content:center;margin-right:14px}
.btn-dark{background:var(--grey-btn);color:#fff;border-radius:20px;display:flex;align-items:center;justify-content:center;font-size:9px;font-weight:600}
.socials{left:0;top:319px;width:187px;height:38px;display:flex}
.socials span{flex:1;display:flex;align-items:center;justify-content:center}
.socials i{width:12px;height:12px;border-radius:50%;background:#fff;display:block}
.profile-foot{left:0;top:357px;width:187px;height:6px;background:#444}
.upload{left:391px;top:54px;width:187px;height:238px;background:var(--teal)}
.drop{left:9px;top:31px;width:169px;height:197px;background:#fff}
.file{left:8px;top:114px;width:155px;font-size:8px;font-weight:400;color:#444}
.bar{left:28px;top:138px;width:132px;height:3px;background:#cde}
.bar b{display:block;width:70px;height:3px;background:#2f7fc0}
.btn-pink{left:9px;top:156px;width:150px;height:34px;border-radius:18px;background:var(--pink);color:#fff;font-size:8.5px;display:flex;align-items:center;justify-content:center;gap:3px}
.brand-colors{left:1013px;top:54px;width:181px;height:361px;background:var(--pink)}
.picker{left:6px;top:80px;width:156px;height:272px;background:#fff;margin-left:0}
.label{font-size:7.5px;font-weight:400;color:#444;letter-spacing:.4px}
.swatches{left:6px;top:38px;display:flex;gap:4px}
.swatches i{width:12px;height:12px;border-radius:50%;display:block}
.sat{left:6px;top:60px;width:120px;height:120px;background:linear-gradient(to top,#000,transparent),linear-gradient(to right,#fff,#e8442a)}
.hue{left:132px;top:60px;width:18px;height:120px;background:linear-gradient(#f00,#ff0,#0f0,#0ff,#00f,#f0f,#f00)}
.hex{left:6px;top:188px;width:144px;height:20px;border:1px solid #e5e5e5;display:flex;align-items:center;padding:0 6px;font-size:8px;font-weight:400;justify-content:space-between}
.contrast{left:6px;top:240px;width:148px;height:19px;border:1px solid #e5e5e5;display:flex;font-size:6.5px;font-weight:600}
.contrast span{flex:1;display:flex;align-items:center;justify-content:center}
.save{left:1029px;top:673px;width:150px;height:34px;font-size:10px;font-weight:400;letter-spacing:.5px}
.grip{position:absolute;right:3px;bottom:3px;width:5px;height:5px;border-right:1px solid #bbb;border-bottom:1px solid #bbb}
</style>
</head>
<body>
<header class="abs topbar">
  <div class="abs brand">BLOOMWISE</div>
  <div class="abs tab active">Plan</div>
  <div class="abs tab" style="left:300px;width:52px">Learn</div>
  <div class="abs tab" style="left:400px;width:75px">Remember</div>
  <div class="abs account">
    <svg width="10" height="10" viewBox="0 0 10 10"><circle cx="5" cy="3" r="2.4" fill="#fff"/><path d="M0.5 10a4.5 4 0 0 1 9 0z" fill="#fff"/></svg>
    <span>My Profile</span><span>|</span>
    <svg width="10" height="10" viewBox="0 0 10 10"><path d="M3 2.2a3.8 3.8 0 1 0 4 0" stroke="#fff" stroke-width="1.4" fill="none"/><line x1="5" y1="0.5" x2="5" y2="5" stroke="#fff" stroke-width="1.4"/></svg>
    <span>Logout</span>
  </div>
</header>

<nav class="abs sidebar">
  <div class="nav-item light"><span class="ico"></span>Your Business<span style="margin-left:auto;margin-right:24px">⌄</span></div>
  <div class="nav-sub"><span class="ico" style="width:7px;height:7px"></span>Who You Are</div>
  <div class="nav-sub alt"><span class="ico" style="width:7px;height:7px"></span>Why You Exist</div>
  <div class="nav-item"><span class="ico"></span>Your Products</div>
  <div class="nav-item light"><span class="ico"></span>Your Customers</div>
  <div class="nav-item"><span class="ico"></span>Your Goals</div>
  <div class="nav-item"><span class="ico"></span>Your Plans</div>
  <div class="abs copyright">© 2017, all Rights Reserved,<br>Bloomwise</div>
</nav>

<section class="card profile">
  <div class="abs logo-ring">Lark &amp; Lace</div>
  <div class="abs profile-name">LARK &amp; LACE</div>
  <div class="abs contact" style="top:187px"><span class="badge" style="background:#2f84b4"><i class="ico" style="border-color:#fff;width:14px;height:14px"></i></span>www.larkandlace.com</div>
  <div class="abs contact" style="top:222px"><span class="badge" style="background:#f06bb0"><i class="ico" style="border-color:#fff;width:14px;height:14px"></i></span>hello@larkandlace.com</div>
  <div class="abs btn-dark" style="left:18px;top:272px;width:150px;height:34px">Edit Info</div>
  <div class="abs socials">
    <span style="background:#3b5e9c"><i></i></span><span style="background:#3ea6e0"><i></i></span><span style="background:#dc4a36"><i></i></span><span style="background:#b4348a"><i></i></span>
  </div>
  <div class="abs profile-foot"></div>
</section>

<section class="card upload">
  <div class="card-head" style="height:30px">UPLOAD NEW LOGO</div>
  <div class="abs drop">
    <svg class="abs" style="left:49px;top:38px" width="72" height="48" viewBox="0 0 72 48"><rect x="2" y="6" width="34" height="36" rx="2" fill="#8fd19e" transform="rotate(-10 19 24)"/><rect x="34" y="4" width="34" height="36" rx="2" fill="#f3dd6b" transform="rotate(8 51 22)"/><rect x="10" y="30" width="26" height="10" fill="#2e9b56"/><rect x="38" y="30" width="26" height="10" fill="#2e9b56"/><text x="14" y="38" font-size="7" fill="#fff" font-family="Montserrat,sans-serif" font-weight="700">JPG</text><text x="42" y="38" font-size="7" fill="#fff" font-family="Montserrat,sans-serif" font-weight="700">PNG</text></svg>
    <svg class="abs" style="left:8px;top:124px" width="14" height="18" viewBox="0 0 14 18"><path d="M0 0h9l5 5v13H0z" fill="#68c7ff"/></svg>
    <div class="abs file" style="left:32px">image_01.jpg<br><span style="font-size:6px">2.7mb of 4.1mb</span></div>
    <div class="abs" style="left:150px;top:121px;font-size:8px;color:#e33;font-weight:700">✕</div>
    <div class="abs bar"><b></b></div>
    <div class="abs btn-pink">Drag files here or <b style="font-weight:600">Browse</b></div>
  </div>
</section>

<section class="card" style="left:586px;top:54px;width:186px;height:100px;background:var(--teal)">
  <div class="card-head" style="background:var(--teal-deep)">BUSINESS NAME</div>
  <p class="hint">Insert business / company name</p>
  <div class="field" style="left:9px;top:64px;width:169px;height:25px"></div>
</section>

<section class="card" style="left:586px;top:162px;width:186px;height:130px;background:var(--teal)">
  <div class="card-head" style="background:var(--teal-deep)">BUSINESS TAG LINE</div>
  <p class="hint" style="padding-top:12px">Explain the value of your business in 5 words or less</p>
  <div class="field" style="left:9px;top:79px;width:169px;height:25px"></div>
</section>

<section class="card" style="left:782px;top:54px;width:225px;height:238px;background:var(--teal)">
  <div class="card-head" style="background:var(--teal-deep)">BIO</div>
  <p class="hint">Who are you? What do you do? This type of information you'd have in "about" page of your website.</p>
  <div class="field" style="left:7px;top:83px;width:211px;height:147px"><i class="grip"></i></div>
</section>

<section class="card brand-colors">
  <div class="card-head" style="background:var(--pink-deep)">SELECT BRAND COLORS</div>
  <p class="hint">Choose your brand colrs. You can use custom code also</p>
  <div class="abs picker">
    <div class="abs label" style="left:6px;top:20px">PICK A SWATCH</div>
    <div class="abs swatches">
      <i style="background:#5b9be0"></i><i style="background:#67c27a"></i><i style="background:#f2d13b"></i><i style="background:#f39a3b"></i><i style="background:#ec5656"></i><i style="background:#ee8ec0"></i><i style="background:#5b5ad0"></i><i style="background:#555"></i><i style="background:#fff;border:1px solid #ccc"></i>
    </div>
    <div class="abs sat"><i class="abs" style="left:91px;top:21px;width:8px;height:8px;border:1.5px solid #fff;border-radius:50%"></i></div>
    <div class="abs hue"><i class="abs" style="left:0;top:6px;width:18px;height:2px;background:#fff"></i></div>
    <div class="abs hex"><span>✎ #E2453B</span><i style="width:12px;height:12px;border-radius:50%;background:#e2453b;display:block"></i></div>
    <div class="abs label" style="left:6px;top:224px">UI CONTRAST</div>
    <div class="abs contrast"><span style="background:#e8e8e8">☼ LIGHT</span><span>◐ DARK</span></div>
  </div>
</section>

<section class="card" style="left:391px;top:298px;width:614px;height:118px;background:var(--blue)">
  <div class="card-head" style="background:var(--blue-deep)">VISION</div>
  <p class="hint" style="padding-top:11px">What do you want to achieve in the next 12-18 months? Think about this from your customer's perspective. What problem are you trying to solve? What is your vision for solving this problem?</p>
  <div class="field" style="left:6px;top:76px;width:600px;height:36px"><i class="grip"></i></div>
</section>

<section class="card" style="left:198px;top:423px;width:187px;height:245px;background:var(--blue)">
  <div class="card-head" style="background:var(--blue-deep)">KEY COMPETITORS</div>
  <p class="hint" style="padding-top:12px">Who are the industry players who you aspire to? Who are the ones most similar to you now? Who are all of the people that can help solve the same problem you do for potential customers</p>
  <div class="field" style="left:6px;top:119px;width:174px;height:120px"><i class="grip"></i></div>
</section>

<section class="card" style="left:391px;top:423px;width:803px;height:245px;background:var(--light)">
  <div class="card-head" style="background:var(--side)">SWOT ANALYSIS</div>
</section>

<section class="card" style="left:402px;top:473px;width:187px;height:187px;background:var(--teal)">
  <div class="card-head" style="background:var(--teal-deep)">STRENGTHS</div>
  <p class="hint" style="padding-top:12px">Who are the industry players who you aspire to? Who are the ones most similar to you now? Who are all of the people that can help solve the same problem you do for potential customers</p>
  <div class="field" style="left:6px;top:117px;width:175px;height:63px"><i class="grip"></i></div>
</section>
<section class="card" style="left:600px;top:473px;width:187px;height:187px;background:var(--pink)">
  <div class="card-head" style="background:var(--pink-deep)">WEEKNESS</div>
  <p class="hint" style="padding-top:12px">Where are the competitors better than you? What challenges do you have when it comes to operating your business, growing your business, or serving your customers?</p>
  <div class="field" style="left:6px;top:117px;width:175px;height:63px"><i class="grip"></i></div>
</section>
<section class="card" style="left:798px;top:473px;width:187px;height:187px;background:var(--blue)">
  <div class="card-head" style="background:var(--blue-deep)">OPPORTUNITIES</div>
  <p class="hint" style="padding-top:12px">What changes are happening in your industry, in technology, or in the world around you ( the environment, politics, government etc.) that you can take advantage of?</p>
  <div class="field" style="left:6px;top:117px;width:175px;height:63px"><i class="grip"></i></div>
</section>
<section class="card" style="left:997px;top:473px;width:187px;height:187px;background:var(--pink)">
  <div class="card-head" style="background:var(--pink-deep)">THREATS</div>
  <p class="hint" style="padding-top:12px">What changes are happening in your industry, in technology, or in the world around you ( the environment, politics, government etc.) that are threat to your business?</p>
  <div class="field" style="left:6px;top:117px;width:175px;height:63px"><i class="grip"></i></div>
</section>

<div class="abs btn-dark save">Save Changes</div>
</body>
</html>
```